We need a design for our retail display and for our stockist's retail display.
Our product is fresh corn tortillas. These can be used to make tacos, quesadillas, tortilla chips and tostadas.
We want the table talker to use our brand style (see our website) and show the tortillas versatility.
verdel-foods.co.uk
It should also have a space for our stockists to write in a blank space under the heading "Our fresh tortillas are delivered every....[blank space]"
The table talker should be 75mm tall x 150mm wide. This will also have a 25mm self adhesive flap at the top which can be blank or the same colour as the background.
Please feel free to use any files from our website as well as illustrations attached.
Customers in high end shops and delis
food and drink

```html
<!DOCTYPE html>
<html lang="en">
<head>
<meta charset="utf-8">
<title>Verdel Foods – Fresh Corn Tortillas Table Talker</title>
<link rel="stylesheet" href="https://fonts.googleapis.com/css2?family=Barlow+Condensed:wght@600;700&family=Kaushan+Script&family=Montserrat:wght@500&family=Open+Sans:wght@600&display=swap">
<style>
  :root {
    --stage: #b1b1b1;
    --navy: #1f2d4b;
    --navy-deep: #0c2346;
    --gold: #e6c200;
    --gold-soft: #f2d34a;
    --white: #ffffff;
    --ink: #141414;
  }
  * { margin: 0; padding: 0; box-sizing: border-box; }
  html, body {
    width: 1200px; height: 708px; overflow: hidden;
    background: var(--stage);
  }
  .table-talker {
    position: absolute; left: 94px; top: 90px;
    width: 1029px; height: 514px;
    background: var(--white);
    overflow: hidden;
    box-shadow: 0 4px 10px rgba(0,0,0,0.25);
  }
  .backdrop { position: absolute; inset: 0; }

  .brand-mark {
    position: absolute; left: 112px; top: 16px;
    width: 180px; height: 180px;
    border: 2px solid var(--gold);
    border-radius: 50%;
    display: flex; flex-direction: column; align-items: center; justify-content: center;
  }
  .brand-mark__name {
    font-family: "Barlow Condensed", sans-serif; font-weight: 700;
    color: var(--gold); font-size: 36px; line-height: 1; letter-spacing: 3px;
    text-align: center;
  }

  .product-tab {
    position: absolute; left: 390px; top: 0;
    width: 72px; height: 177px;
    background: var(--gold);
    border-bottom-left-radius: 34px;
  }
  .product-tab__text {
    position: absolute; left: 50%; top: 50%;
    transform: translate(-50%, -50%) rotate(-90deg);
    font-family: "Montserrat", sans-serif; font-weight: 500;
    color: var(--navy-deep); font-size: 17px; line-height: 1.2;
    letter-spacing: 0.5px; white-space: nowrap; text-align: left;
  }

  .headline {
    position: absolute; left: 497px; top: 52px; width: 460px;
    font-family: "Barlow Condensed", sans-serif; font-weight: 700;
    text-align: center; line-height: 0.86;
  }
  .headline__top { color: var(--gold); font-size: 98px; letter-spacing: 0; }
  .headline__main { color: var(--white); font-size: 96px; letter-spacing: 1px; }
  .headline__tail {
    font-family: "Kaushan Script", cursive; font-weight: 400;
    color: var(--gold); font-size: 54px; line-height: 1.1; margin-top: 2px;
    margin-left: -36px;
  }

  .claims { position: absolute; left: 935px; top: 36px; width: 88px; }
  .claim {
    position: absolute; left: 0;
    width: 88px; height: 88px; border-radius: 50%;
    background: var(--navy);
    display: flex; flex-direction: column; align-items: center; justify-content: center;
    color: var(--gold); text-align: center;
  }
  .claim::before {
    content: ""; position: absolute; inset: 8px;
    border: 2px solid var(--gold); border-radius: 50%;
  }
  .claim__script { font-family: "Kaushan Script", cursive; font-size: 22px; line-height: 1; }
  .claim__caps { font-family: "Barlow Condensed", sans-serif; font-weight: 600; font-size: 15px; line-height: 1.05; }
  .claim__big { font-family: "Barlow Condensed", sans-serif; font-weight: 700; font-size: 26px; line-height: 0.95; }
  .claim__small { font-family: "Barlow Condensed", sans-serif; font-weight: 600; font-size: 10px; line-height: 1.2; }

  .delivery {
    position: absolute; left: 46px; top: 238px; width: 416px; height: 68px;
    display: flex; align-items: center;
  }
  .delivery__label {
    width: 176px; text-align: center;
    font-family: "Montserrat", sans-serif; font-weight: 500;
    font-size: 15.5px; line-height: 1.22; color: var(--ink);
  }
  .delivery__blank {
    position: absolute; left: 190px; top: 0;
    width: 226px; height: 68px;
    border: 3px solid var(--gold); border-radius: 34px;
  }

  .uses { position: absolute; left: 0; top: 330px; width: 820px; height: 160px; }
  .use { position: absolute; top: 0; width: 170px; text-align: center; }
  .use__name {
    font-family: "Open Sans", sans-serif; font-weight: 600;
    font-size: 21px; line-height: 1; color: var(--ink); letter-spacing: 0.3px;
    height: 20px;
  }
  .use__art {
    margin: 20px auto 0; width: 118px; height: 108px; border-radius: 14px;
    background: radial-gradient(ellipse at center, #d9d9d9 0%, #efefef 60%, #ffffff 100%);
  }
  .use--tall .use__art { margin-top: 30px; }
  .use--tall .use__name { line-height: 0.98; }
  .divider {
    position: absolute; top: 43px; width: 2px; height: 67px; background: var(--gold);
  }
</style>
</head>
<body>
  <section class="table-talker" aria-label="Fresh corn tortillas table talker">
    <svg class="backdrop" width="1029" height="514" viewBox="0 0 1029 514" aria-hidden="true">
      <defs>
        <linearGradient id="navyShade" x1="0" y1="0" x2="1" y2="1">
          <stop offset="0" stop-color="#25355a"/>
          <stop offset="1" stop-color="#0c2346"/>
        </linearGradient>
      </defs>
      <rect x="0" y="0" width="470" height="218" fill="#24324f"/>
      <path d="M440 0 H1029 V262 C995 270 965 285 951 304 H520 C482 300 462 262 455 218 H440 Z" fill="url(#navyShade)"/>
      <path d="M839 514 C858 400 925 300 1029 259 V514 Z" fill="#e6c200"/>
    </svg>

    <div class="brand-mark">
      <span class="brand-mark__name">VERDEL<br>FOODS</span>
    </div>

    <div class="product-tab">
      <div class="product-tab__text">SOFT CORN<br>TORTILLA</div>
    </div>

    <h1 class="headline">
      <div class="headline__top">FRESH CORN</div>
      <div class="headline__main">TORTILLAS</div>
      <div class="headline__tail">and other</div>
    </h1>

    <div class="claims">
      <div class="claim" style="top:0"><span class="claim__script">vegan</span></div>
      <div class="claim" style="top:88px"><span class="claim__script">gluten</span><span class="claim__caps">FREE</span></div>
      <div class="claim" style="top:181px"><span class="claim__big">NO<br>GMO</span></div>
      <div class="claim" style="top:274px"><span class="claim__caps">100%</span><span class="claim__small">BIODEGRADABLE<br>RECYCLABLE</span></div>
      <div class="claim" style="top:367px"><span class="claim__script">no</span><span class="claim__small">PRESERVATIVES</span></div>
    </div>

    <div class="delivery">
      <p class="delivery__label">Our fresh tortillas are delivered every.</p>
      <div class="delivery__blank" aria-label="Space for stockist to write delivery day"></div>
    </div>

    <div class="uses">
      <div class="use" style="left:4px">
        <div class="use__name">TACOS</div>
        <div class="use__art" role="img" aria-label="Line illustration of a taco"></div>
      </div>
      <span class="divider" style="left:162px"></span>
      <div class="use" style="left:167px">
        <div class="use__name">QUESADILLAS</div>
        <div class="use__art" role="img" aria-label="Line illustration of a quesadilla wedge"></div>
      </div>
      <span class="divider" style="left:334px"></span>
      <div class="use use--tall" style="left:333px">
        <div class="use__name">TORTILLA<br>CHIPS</div>
        <div class="use__art" role="img" aria-label="Line illustration of a tortilla chip dipped in salsa"></div>
      </div>
      <span class="divider" style="left:480px"></span>
      <div class="use" style="left:478px">
        <div class="use__name">TAQUITOS</div>
        <div class="use__art" role="img" aria-label="Line illustration of a rolled taquito"></div>
      </div>
      <span class="divider" style="left:633px"></span>
      <div class="use" style="left:638px">
        <div class="use__name">TOSTADAS</div>
        <div class="use__art" role="img" aria-label="Line illustration of a topped tostada"></div>
      </div>
    </div>
  </section>
</body>
</html>
```